Medical Staffing Pamphlet

We are starting to staff for Medical positions for the first time, we need pamphlets to take to medical facilities to try to gain new business

Need an copy to edit, many errors.

```html
<!DOCTYPE html>
<html lang="en">
<head>
<meta charset="utf-8">
<title>Meridian Staffing Medical – Tri-fold Pamphlet</title>
<link rel="stylesheet" href="https://fonts.googleapis.com/css2?family=Saira:wght@400;500;600&family=Saira+Semi+Condensed:wght@400;500&family=Saira+Condensed:wght@500;600;700&display=swap">
<style>
  :root{
    --navy:#1f2670;
    --royal:#1b4382;
    --band-blue:#1f5fae;
    --sky:#aedcf7;
    --sky-text:#a9d9f6;
    --green:#1aa050;
    --paper:#ffffff;
    --rule:#c9ccd3;
    --backdrop:#ffffff;
  }
  *{box-sizing:border-box;margin:0;padding:0}
  html,body{width:1200px;height:1200px;overflow:hidden;background:var(--backdrop)}
  body{position:relative;font-family:"Saira",sans-serif;color:var(--navy)}

  .sheet{position:absolute;left:280px;width:639px;height:483px;background:var(--paper);
    box-shadow:4px 6px 14px rgba(0,0,0,.22);overflow:hidden}
  .sheet--outside{top:101px}
  .sheet--inside{top:611px}

  .panel{position:absolute;top:0;height:100%;width:213px}
  .panel--1{left:0}
  .panel--2{left:213px;width:213px;border-left:1px solid var(--rule);border-right:1px solid var(--rule)}
  .panel--3{left:426px;width:213px}

  /* outside: panel 1 */
  .icon-spot{position:absolute;border-radius:6px}
  .icon-spot--stethoscope{left:60px;top:40px;width:92px;height:100px;
    background:linear-gradient(160deg,#e6f2ea,#dfe3f3)}
  .promise-band{position:absolute;left:0;top:179px;width:100%;height:158px;background:var(--sky);
    display:flex;align-items:center;justify-content:center;text-align:center;white-space:nowrap;
    font-family:"Saira Semi Condensed",sans-serif;font-size:19px;line-height:26px;font-weight:400;color:var(--navy)}
  .brand-mark{position:absolute;display:flex;align-items:center;gap:8px;white-space:nowrap;
    font-family:"Saira Condensed",sans-serif;font-weight:700;letter-spacing:.5px}
  .brand-mark__square{width:16px;height:16px;flex:none}
  .brand-mark--panel1{left:0;width:100%;top:385px;height:36px;justify-content:center;font-size:24px;color:var(--navy)}
  .brand-mark--panel1 .brand-mark__square{background:var(--navy)}

  /* outside: panel 2 */
  .photo{position:absolute;left:0;width:100%}
  .photo--office{top:0;height:143px;background:linear-gradient(135deg,#c9ccd2 0%,#9ea3ad 55%,#6f7480 100%)}
  .contact-title{position:absolute;top:152px;width:100%;text-align:center;white-space:nowrap;
    font-family:"Saira Condensed",sans-serif;font-weight:700;font-size:26px;line-height:33px;color:var(--navy)}
  .contact-band{position:absolute;top:312px;width:100%;height:26px;background:var(--sky);white-space:nowrap;
    color:#fff;text-align:center;font-size:23px;line-height:26px;font-weight:400;letter-spacing:.5px}
  .contact-address{position:absolute;top:345px;width:100%;text-align:center;white-space:nowrap;
    font-family:"Saira Semi Condensed",sans-serif;font-size:17px;line-height:21px;font-style:normal}
  .contact-web{position:absolute;top:425px;width:100%;text-align:center;font-size:12.5px;white-space:nowrap}

  /* outside: panel 3 (cover) */
  .panel--cover{background:var(--royal);border:none}
  .brand-mark--cover{left:0;width:100%;top:64px;height:116px;justify-content:center;
    font-size:22px;color:#fff}
  .brand-mark--cover .brand-mark__square{background:#fff}
  .cover-title{position:absolute;top:200px;width:100%;text-align:center;white-space:nowrap;
    font-family:"Saira Condensed",sans-serif;font-weight:600;font-size:46px;line-height:54px;color:var(--sky-text);letter-spacing:1px}
  .cover-tagline{position:absolute;top:392px;width:100%;text-align:center;white-space:nowrap;color:#d9efff;
    font-family:"Saira Semi Condensed",sans-serif;font-size:16px;line-height:18px}

  /* inside */
  .photo--team{top:0;height:276px;background:linear-gradient(180deg,#d7ecf7 0%,#8fc7e4 45%,#4c8fc4 100%)}
  .section-band{position:absolute;left:0;top:240px;width:100%;height:58px}
  .section-label{position:absolute;top:266px;font-family:"Saira Condensed",sans-serif;font-weight:600;
    font-size:25px;line-height:30px;color:#fff;letter-spacing:.3px;white-space:nowrap}
  .section-label--left{left:11px}
  .section-label--right{right:10px}

  .inside-body{position:absolute;top:298px;height:185px}
  .inside-body.panel--2{border-left:1px solid var(--rule);border-right:1px solid var(--rule)}
  .about-text{position:absolute;left:8px;top:10px;width:196px;font-size:9.4px;line-height:14px;text-align:justify;color:var(--navy)}
  .icon-spot--capsule{left:86px;top:102px;width:28px;height:26px;background:linear-gradient(135deg,#dfe5f6,#bfcbe8)}
  .trust-text{position:absolute;top:12px;width:100%;text-align:center;white-space:nowrap;
    font-family:"Saira Semi Condensed",sans-serif;font-size:19px;line-height:27px;font-weight:400;letter-spacing:.3px}

  .services{position:absolute;left:8px;top:6px;width:200px}
  .services__heading{font-family:"Saira Condensed",sans-serif;font-weight:700;font-size:11px;line-height:14px;color:var(--royal)}
  .services__list{list-style:none;font-size:9.2px;line-height:14.2px;font-weight:500;text-transform:uppercase;margin-bottom:6px;white-space:nowrap}
  .icon-spot--clipboard{left:138px;top:62px;width:26px;height:36px;border-radius:3px;background:linear-gradient(180deg,#eef3fb,#d4deef)}
</style>
</head>
<body>

<section class="sheet sheet--outside" aria-label="Pamphlet outside">
  <div class="panel panel--1">
    <div class="icon-spot icon-spot--stethoscope" role="img" aria-label="Stethoscope icon in navy and green"></div>
    <p class="promise-band">OUR MEDICAL<br>STAFFING SPECIALIST<br>WILL PROVIDE YOU<br>QUALITY EMPLOYEES</p>
    <div class="brand-mark brand-mark--panel1"><span class="brand-mark__square"></span><span>MERIDIAN</span></div>
  </div>

  <div class="panel panel--2">
    <div class="photo photo--office" role="img" aria-label="Photo of hands signing paperwork at an office desk"></div>
    <h2 class="contact-title">MERIDIAN STAFFING<br>MEDICAL</h2>
    <h3 class="contact-band">CONTACT US</h3>
    <address class="contact-address">2450 N. Lakeview Rd.<br>Fairmont, Indiana 47000<br>812-555-0142</address>
    <p class="contact-web">meridianstaffingservices.com</p>
  </div>

  <div class="panel panel--3 panel--cover">
    <div class="brand-mark brand-mark--cover"><span class="brand-mark__square"></span><span>MERIDIAN</span></div>
    <h1 class="cover-title">MERIDIAN<br>STAFFING<br>MEDICAL</h1>
    <p class="cover-tagline">Providing high quality<br>healthcare professionals</p>
  </div>
</section>

<section class="sheet sheet--inside" aria-label="Pamphlet inside">
  <div class="photo photo--team" role="img" aria-label="Group photo of smiling doctors and nurses in scrubs and white coats"></div>

  <svg class="section-band" viewBox="0 0 639 58" preserveAspectRatio="none" aria-hidden="true">
    <path d="M0 14 Q320 36 639 4 L639 58 L0 58 Z" fill="var(--band-blue)"/>
    <path d="M0 14 Q320 36 639 4 L639 12 Q320 46 0 24 Z" fill="#ffffff"/>
  </svg>
  <h2 class="section-label section-label--left">WHO WE ARE</h2>
  <h2 class="section-label section-label--right">OUR SERVICES</h2>

  <div class="panel panel--1 inside-body">
    <p class="about-text">Meridian Staffing is the largest locally owned recruiting company in the TriState. We began building staffing partnerships are the foundation of our success. We provide customized staffing solutions for the many industries we service, including medical.</p>
    <div class="icon-spot icon-spot--capsule" role="img" aria-label="Small capsule pills icon"></div>
  </div>

  <div class="panel panel--2 inside-body">
    <p class="trust-text">PUT YOUR TRUST<br>IN US, AND WE WILL<br>TAKE CARE OF<br>YOUR MEDICAL<br>STAFFING NEEDS.</p>
  </div>

  <div class="panel panel--3 inside-body">
    <div class="services">
      <h3 class="services__heading">ADMINISTRATIVE</h3>
      <ul class="services__list">
        <li>Billing Specialists</li>
        <li>Coding Specialists</li>
        <li>Medical Records</li>
        <li>Office Managers</li>
        <li>Receptionists</li>
      </ul>
      <h3 class="services__heading">CLINICAL</h3>
      <ul class="services__list">
        <li>Certified Medical Assistants</li>
        <li>Registered Medical Assistants</li>
        <li>Certified Nursing Assistants</li>
        <li>Phlebotomists</li>
      </ul>
    </div>
    <div class="icon-spot icon-spot--clipboard" role="img" aria-label="Clipboard with heartbeat line icon"></div>
  </div>
</section>

</body>
</html>
```